Business Card

I need a business card for a nutrition/fitness consultant. We are a personalized and online service that caters to developing individual plans based on persons needs. I will send you information to need on card as well as logo. Last business card was grey background and writing was black and red. I think a pic on the backside (maybe a photo that is on the app) would be good?

HelloMarlo (Ill send you logo)
Marlo Venti, Registered Nurse and Certified Sports Nutrionist (R.N., C.S.N.)
Personalized Nutrition and Fitness Architecture

1-800-555-0147 office
(305) 555-0182 cell
website www.hellomarlo-demo.com
marlo@hellomarlo-demo.com

Two locations so maybe two cards
2180 Willowbend Lane, inside Sunpeak Glow Studio
Palm Vista, Fl 33199

and
7300 W Orchard Parkway
Boca Raton, Florida 33498

Requirements
Must have
• I guess the logo we provide so it is consistent with the new website etc

```html
<!DOCTYPE html>
<html lang="en">
<head>
<meta charset="utf-8">
<title>HelloMarlo Business Card</title>
<link rel="stylesheet" href="https://fonts.googleapis.com/css2?family=Questrial&family=Josefin+Sans:wght@600;700&display=swap">
<style>
  :root {
    --page: #e8e6e3;
    --card-light: #eeeeee;
    --card-mid: #c9c9c9;
    --card-dark: #a9a9a9;
    --brand-red: #e3232b;
    --ink: #1b1b1b;
    --white: #ffffff;
    --photo-light: #d8d8d8;
    --photo-dark: #6f6f6f;
  }
  * { box-sizing: border-box; margin: 0; padding: 0; }
  html, body {
    width: 1200px; height: 1200px; overflow: hidden;
    background: var(--page);
  }
  .sheet { position: relative; width: 1200px; height: 1200px; }
  .card {
    position: absolute; left: 110px; width: 980px; height: 560px;
    overflow: hidden;
    background: linear-gradient(160deg, var(--card-light) 0%, var(--card-mid) 55%, var(--card-dark) 100%);
    box-shadow: 0 6px 18px rgba(0,0,0,0.18);
    font-family: "Questrial", "Century Gothic", sans-serif;
    color: var(--ink);
  }
  .card--front { top: 30px; }
  .card--back { top: 610px; }

  /* Wordmark */
  .wordmark {
    position: absolute; display: flex; align-items: center; gap: 14px;
    font-family: "Questrial", "Century Gothic", sans-serif;
    color: var(--ink); letter-spacing: 1px; white-space: nowrap;
  }
  .wordmark__dot { display: block; border-radius: 50%; background: var(--brand-red); flex: none; }

  /* Front side */
  .front__tagline {
    position: absolute; top: 52px; right: 44px; white-space: nowrap;
    font-family: "Josefin Sans", "Century Gothic", sans-serif; font-weight: 700;
    font-size: 21px; letter-spacing: 1px; text-transform: uppercase;
  }
  .front__wordmark { top: 110px; left: 60px; font-size: 72px; }
  .front__wordmark .wordmark__dot { width: 30px; height: 30px; }

  .front__band {
    position: absolute; top: 262px; left: 0; width: 100%; height: 112px;
    background: var(--brand-red); color: var(--white);
    display: flex; flex-direction: column; justify-content: center; gap: 8px;
    padding: 0 44px;
  }
  .front__name { font-size: 30px; padding-left: 340px; letter-spacing: 0.5px; }
  .front__title {
    font-family: "Josefin Sans", "Century Gothic", sans-serif; font-weight: 600;
    font-size: 23px; letter-spacing: 0.5px; white-space: nowrap;
  }

  .front__contacts {
    position: absolute; left: 44px; top: 400px; list-style: none;
    display: flex; flex-direction: column; gap: 6px; color: var(--white);
  }
  .contact { display: flex; align-items: center; gap: 14px; font-size: 21px; white-space: nowrap; }
  .contact--large { font-size: 27px; }
  .contact svg { width: 24px; height: 24px; flex: none; }

  .front__address {
    position: absolute; left: 560px; top: 404px;
    display: flex; gap: 16px; align-items: flex-start;
  }
  .front__address svg { width: 30px; height: 40px; flex: none; margin-top: 6px; }
  .front__address p {
    font-family: "Josefin Sans", "Century Gothic", sans-serif; font-weight: 700;
    font-size: 21px; line-height: 1.2; white-space: nowrap;
  }

  /* Back side */
  .back__panel { position: absolute; left: 0; top: 0; width: 620px; height: 100%; }
  .back__wordmark { top: 110px; left: 90px; font-size: 90px; }
  .back__wordmark .wordmark__dot { width: 36px; height: 36px; }
  .back__band {
    position: absolute; left: 0; top: 310px; width: 620px; height: 86px;
    background: var(--brand-red); color: var(--white);
    display: flex; align-items: center; padding-left: 36px; white-space: nowrap;
    font-family: "Josefin Sans", "Century Gothic", sans-serif; font-weight: 600;
    font-size: 19px; letter-spacing: 1px; text-transform: uppercase;
  }
  .back__divider {
    position: absolute; left: 620px; top: 0; width: 16px; height: 100%;
    background: var(--brand-red);
  }
  .back__photo {
    position: absolute; left: 636px; top: 0; right: 0; height: 100%;
    background: radial-gradient(circle at 40% 35%, var(--photo-light) 0%, #a6a6a6 50%, var(--photo-dark) 100%);
  }
</style>
</head>
<body>
<main class="sheet">

  <section class="card card--front" aria-label="Business card, contact side">
    <p class="front__tagline">Tailored Meal &amp; Training Blueprints</p>

    <div class="wordmark front__wordmark">
      <span class="wordmark__name">HelloMarlo</span>
      <span class="wordmark__dot"></span>
    </div>

    <div class="front__band">
      <p class="front__name">Marlo Venti</p>
      <p class="front__title">Registered Nurse and Certified Sports Nutrionist (R.N., C.S.N.)</p>
    </div>

    <ul class="front__contacts">
      <li class="contact">
        <svg viewBox="0 0 24 24" aria-hidden="true"><rect x="2" y="5" width="20" height="14" fill="#e3232b"/><path d="M2 5l10 8 10-8" fill="none" stroke="#fff" stroke-width="1.6"/></svg>
        marlo@hellomarlo-demo.com
      </li>
      <li class="contact">
        <svg viewBox="0 0 24 24" aria-hidden="true"><g fill="none" stroke="#e3232b" stroke-width="1.8"><circle cx="12" cy="12" r="9.5"/><ellipse cx="12" cy="12" rx="4.2" ry="9.5"/><path d="M2.5 12h19M4 7h16M4 17h16"/></g></svg>
        website www.hellomarlo-demo.com
      </li>
      <li class="contact contact--large">
        <svg viewBox="0 0 24 24" aria-hidden="true"><path d="M7 2c1 0 2 3 2.5 4.5.3 1-1.5 2-1.5 3 0 2 4.5 7 6.5 7 1 0 2-1.8 3-1.5 1.5.5 4.5 1.5 4.5 2.5 0 2-2.5 4.5-4.5 4.5C10 22 2 14 2 7c0-2 3-5 5-5z" fill="#e3232b"/></svg>
        (305) 555-0182
      </li>
      <li class="contact contact--large">
        <svg viewBox="0 0 24 24" aria-hidden="true"><path d="M2 9c0-3 5-5 10-5s10 2 10 5v2h-5V8.5c-1.5-.6-3.2-.9-5-.9s-3.5.3-5 .9V11H2z" fill="#e3232b"/><path d="M5 13h14l2 8H3z" fill="#e3232b"/><circle cx="12" cy="17" r="2.2" fill="#fff"/></svg>
        1-800-555-0147
      </li>
    </ul>

    <div class="front__address">
      <svg viewBox="0 0 30 40" aria-hidden="true"><path d="M15 1C7.3 1 1 7.2 1 14.8 1 25 15 39 15 39s14-14 14-24.2C29 7.2 22.7 1 15 1z" fill="#e3232b"/><circle cx="15" cy="14.5" r="5.5" fill="#fff"/></svg>
      <p>2180 Willowbend Lane,<br>inside Sunpeak Glow Studio<br>Palm Vista, Fl 33199</p>
    </div>
  </section>

  <section class="card card--back" aria-label="Business card, brand side">
    <div class="back__panel">
      <div class="wordmark back__wordmark">
        <span class="wordmark__name">HelloMarlo</span>
        <span class="wordmark__dot"></span>
      </div>
      <p class="back__band">Tailored Meal &amp; Training Blueprints</p>
    </div>
    <div class="back__divider"></div>
    <div class="back__photo" role="img" aria-label="Black-and-white portrait photo of the consultant holding a red apple beside a plate of red apples"></div>
  </section>

</main>
</body>
</html>
```